Commercial Business Card - stand out, clean, simple, unique.

commercial real estate group located in Texas. Called 4 Pines Real Estate. We want a unique yet clean and professional card. On one side I would like the 4P to be by itself or to look as unique or tasteful as possible. We have the logo in white, black, and color in case a black background or something similar looks best on one side. We need a space for our name, email, cell. website. And possibly room for a phrase or city.

Contact Information for Business Card

Name, Title, Email, Phone Number, website

```html
<!DOCTYPE html>
<html lang="en">
<head>
<meta charset="utf-8">
<title>4 Pines Real Estate — Business Card</title>
<link href="https://fonts.googleapis.com/css2?family=Cinzel:wght@700&family=Lato:wght@400;700&display=swap" rel="stylesheet">
<style>
  :root {
    --backdrop: #3a3b3e;
    --card: #ffffff;
    --navy: #1d2d6b;
    --navy-deep: #14205a;
    --orange: #e2782f;
    --red: #c8352b;
    --ink: #222733;
    --ghost: #eef0f5;
  }
  * { box-sizing: border-box; margin: 0; padding: 0; }
  html, body { width: 1200px; height: 900px; overflow: hidden; }
  body {
    background: var(--backdrop);
    position: relative;
    font-family: "Lato", Arial, sans-serif;
  }
  .card {
    position: absolute;
    width: 560px;
    height: 320px;
    background: var(--card);
    border-radius: 26px;
    overflow: hidden;
    box-shadow: 0 18px 40px rgba(0,0,0,.45);
  }
  .card::after {
    content: "";
    position: absolute;
    left: 0; right: 0; bottom: 0;
    height: 7px;
  }
  .card--front { left: 60px; top: 80px; }
  .card--front::after { background: linear-gradient(90deg, var(--red), var(--orange)); }
  .card--back { left: 580px; top: 500px; }
  .card--back::after { background: linear-gradient(90deg, var(--navy-deep), var(--navy)); }

  .brand {
    display: flex;
    align-items: center;
    gap: 14px;
    white-space: nowrap;
  }
  .brand__mark {
    width: 34px;
    height: 34px;
    background: var(--navy);
    flex: none;
  }
  .brand__name {
    font-family: "Cinzel", Georgia, serif;
    font-weight: 700;
    font-size: 28px;
    line-height: 1;
    letter-spacing: 1px;
    color: var(--navy);
  }

  .card--front .brand {
    position: absolute;
    left: 50%; top: 50%;
    transform: translate(-50%, -50%);
  }

  .card--back .brand {
    position: absolute;
    left: 42px; top: 58px;
    gap: 10px;
  }
  .card--back .brand__mark { width: 24px; height: 24px; }
  .card--back .brand__name { font-size: 20px; }

  .ghost-shape {
    position: absolute;
    right: -30px; top: -10px;
    width: 260px; height: 260px;
    border-radius: 50%;
    background: var(--ghost);
  }

  .person {
    position: absolute;
    left: 200px; top: 128px;
    padding-left: 14px;
    border-left: 1px solid var(--orange);
  }
  .person__name {
    font-family: "Cinzel", Georgia, serif;
    font-weight: 700;
    font-size: 24px;
    color: var(--navy);
    letter-spacing: .5px;
    white-space: nowrap;
  }
  .person__title { font-size: 15px; color: var(--orange); margin-top: 2px; }

  .contacts {
    position: absolute;
    left: 200px; top: 206px;
    padding-left: 14px;
    border-left: 1px solid var(--navy);
    list-style: none;
  }
  .contacts__item {
    display: flex;
    align-items: center;
    gap: 10px;
    font-size: 14px;
    color: var(--ink);
    line-height: 22px;
    white-space: nowrap;
  }
  .contacts__icon { width: 13px; height: 13px; fill: var(--orange); flex: none; }
</style>
</head>
<body>
  <section class="card card--front" aria-label="Card front">
    <div class="brand">
      <span class="brand__mark" aria-hidden="true"></span>
      <span class="brand__name">4 PINES REAL ESTATE</span>
    </div>
  </section>

  <section class="card card--back" aria-label="Card back">
    <span class="ghost-shape" aria-hidden="true"></span>
    <div class="brand">
      <span class="brand__mark" aria-hidden="true"></span>
      <span class="brand__name">4 PINES REAL ESTATE</span>
    </div>

    <div class="person">
      <p class="person__name">DANIEL REYES</p>
      <p class="person__title">Founder &amp; CEO</p>
    </div>

    <ul class="contacts">
      <li class="contacts__item">
        <svg class="contacts__icon" viewBox="0 0 24 24" aria-hidden="true"><path d="M6.6 10.8a15 15 0 0 0 6.6 6.6l2.2-2.2c.3-.3.7-.4 1-.2 1.1.4 2.3.6 3.6.6.6 0 1 .4 1 1V20c0 .6-.4 1-1 1A17 17 0 0 1 3 4c0-.6.4-1 1-1h3.5c.6 0 1 .4 1 1 0 1.3.2 2.5.6 3.6.1.3 0 .7-.2 1z"/></svg>
        555 210 4480
      </li>
      <li class="contacts__item">
        <svg class="contacts__icon" viewBox="0 0 24 24" aria-hidden="true"><path d="M2 5h20v14H2z" opacity=".35"/><path d="M2 5h20l-10 8z"/></svg>
        info@4pinesrealestate.com
      </li>
      <li class="contacts__item">
        <svg class="contacts__icon" viewBox="0 0 24 24" aria-hidden="true"><path d="M12 2a10 10 0 1 0 0 20 10 10 0 0 0 0-20zm6.9 6h-3a15 15 0 0 0-1.3-3.9A8 8 0 0 1 18.9 8zM12 4c.8 1.2 1.5 2.5 1.9 4h-3.8c.4-1.5 1.1-2.8 1.9-4zM4.3 14a8 8 0 0 1 0-4h3.4a16 16 0 0 0 0 4zm.8 2h3a15 15 0 0 0 1.3 3.9A8 8 0 0 1 5.1 16zm3-8h-3a8 8 0 0 1 4.3-3.9C8.8 5.3 8.4 6.6 8.1 8zM12 20c-.8-1.2-1.5-2.5-1.9-4h3.8c-.4 1.5-1.1 2.8-1.9 4zm2.3-6H9.7a14 14 0 0 1 0-4h4.6a14 14 0 0 1 0 4zm.3 5.9c.6-1.200 1-2.5 1.3-3.9h3a8 8 0 0 1-4.3 3.9zm1.7-5.9a16 16 0 0 0 0-4h3.4a8 8 0 0 1 0 4z"/></svg>
        www.4pinesrealestate.com
      </li>
    </ul>
  </section>
</body>
</html>
```